8 x 8 - Social Media Posting - Bright Key DPA Program

Buyer(s) Need Down Payment Assistance?
OUR BRIGHTKEY PROGRAM
offers all you need....
* Grant Up to 3.5% of Purchase Price
* No Down Payment (FHA Only)
* 600 Minimum Score
* No Max DTI Requirement (As Determined by AUS)
* No First Time Home Buyer Requirement
* No Minimum Borrower Contribution
* Non Occupant Co-Borrowers Allowed
Call us today at (800) 417-2960
Harborlane Lending Services, Inc.
7200 Wexmoor Road, Ellicott City, MD 21043
www.harborlanelend.example
NMLS #318674

```html
<!DOCTYPE html>
<html lang="en">
<head>
<meta charset="utf-8">
<title>Bright Key DPA Program – Social Post</title>
<link href="https://fonts.googleapis.com/css2?family=Montserrat:ital,wght@0,500;0,600;0,700;0,800;1,500&display=swap" rel="stylesheet">
<style>
  :root {
    --stage: #e7e2da;
    --brand-blue: #1d45a0;
    --ink: #2b2b2b;
    --body-ink: #3a3633;
    --white: #ffffff;
    --photo-light: #efe9e3;
    --photo-mid: #ddd2c7;
    --photo-warm: #cbbcad;
  }
  * { margin: 0; padding: 0; box-sizing: border-box; }
  html, body {
    width: 1200px; height: 800px; overflow: hidden;
    background: var(--stage);
    font-family: "Montserrat", sans-serif;
  }
  .stage {
    width: 1200px; height: 800px;
    display: flex; align-items: center; justify-content: center;
  }
  .post {
    position: relative;
    width: 720px; height: 720px;
    overflow: hidden;
    box-shadow: 0 10px 30px rgba(0,0,0,0.18);
  }
  .post__photo {
    position: absolute; inset: 0;
    background:
      radial-gradient(ellipse at 50% 45%, var(--photo-warm) 0%, transparent 55%),
      linear-gradient(160deg, var(--photo-light) 0%, var(--photo-mid) 60%, var(--photo-warm) 100%);
  }
  .post__veil {
    position: absolute; inset: 0;
    background: rgba(255,255,255,0.55);
  }
  .post__content {
    position: relative; z-index: 1;
    height: 478px;
    display: flex; flex-direction: column; align-items: center;
    text-align: center;
    padding-top: 46px;
  }
  .brand {
    display: flex; align-items: center; gap: 10px;
    margin-bottom: 34px;
  }
  .brand__dot {
    width: 16px; height: 16px; border-radius: 50%;
    background: var(--brand-blue);
  }
  .brand__name {
    font-weight: 700; font-size: 24px; letter-spacing: 0.04em;
    color: var(--brand-blue); text-transform: uppercase;
  }
  .headline {
    font-weight: 800; font-size: 27px; letter-spacing: 0.01em;
    color: var(--brand-blue); text-transform: uppercase;
    margin-bottom: 16px;
  }
  .program {
    font-weight: 800; font-size: 25px; color: var(--ink);
    text-transform: uppercase; line-height: 1.1;
  }
  .program__tag {
    font-weight: 700; font-size: 22px; color: var(--ink);
    margin-bottom: 16px;
  }
  .benefits {
    list-style: none;
    font-weight: 500; font-size: 20px; line-height: 1.36;
    color: var(--body-ink);
  }
  .benefits li::before {
    content: "•"; margin-right: 6px; font-size: 0.9em;
  }
  .contact {
    position: absolute; left: 0; right: 0; bottom: 0;
    height: 242px; z-index: 1;
    background: var(--brand-blue);
    color: var(--white);
    text-align: center;
    padding-top: 26px;
    font-size: 18px; line-height: 1.3; font-weight: 500;
  }
  .contact__call { font-style: italic; }
  .contact__call strong { font-style: normal; font-weight: 700; }
  .contact__strong { font-weight: 700; }
</style>
</head>
<body>
<main class="stage">
  <article class="post">
    <div class="post__photo" role="img" aria-label="Photo of a smiling woman with outstretched arms in a bright living room among moving boxes"></div>
    <div class="post__veil"></div>

    <section class="post__content">
      <div class="brand">
        <span class="brand__dot"></span>
        <span class="brand__name">Harborlane Lending Services</span>
      </div>
      <h1 class="headline">Buyer(s) Need Down Payment Assistance?</h1>
      <p class="program">Our Brightkey Program</p>
      <p class="program__tag">offers all you need.....</p>
      <ul class="benefits">
        <li>Grant Up to 3.5% of Purchase Price</li>
        <li>No Down Payment (FHA Only)</li>
        <li>600 Minimum Score</li>
        <li>No Max DTI Requirement (As Determined by AUS)</li>
        <li>No First Time Home Buyer Requirement</li>
        <li>No Minimum Borrower Contribution</li>
        <li>Non Occupant Co-Borrowers Allowed</li>
      </ul>
    </section>

    <footer class="contact">
      <p class="contact__call">Call us today at <strong>(800) 417-2960</strong></p>
      <p>Harborlane Lending Services, Inc.</p>
      <p>7200 Wexmoor Road, Larkfield, MD 21790</p>
      <p class="contact__strong">www.harborlanelend.example</p>
      <p class="contact__strong">NMLS #318674</p>
    </footer>
  </article>
</main>
</body>
</html>
```